Website re-design wedding music business

I need my wordpress wedding music website redesigned. I'm a wedding pianist and also provide duo/trio entertainment with other musicians and looking for an overhaul of my wordpress site.

Website: tollykessing.com.au

Target Market(s)

brides; engaged couples

Industry/Entity Type

Wedding

Number of Pages Required

5+ page

Colors

Designer to choose colors to be used in the design.

Requirements
Must have
• I'm looking to overhaul my website which is looking rather tired after 4 years. It is functional but not inviting to visitors. Initially my website started out as a solo piano player providing music for wedding. It is gradually growing now where brides can book
• 1) Solo Piano
• 2) Duo (any combination of Piano / Cello / Vocalist / Violin)
• 3) Trio (any combination of Piano/ Cello /Vocalist / Violin)
• in future it may increase to 4 / 5 /6 piece bands so that needs to be taken into account for the future growth where I'll recruit other musicians.
• Some other functionality I'd like to see
• - Visitors want a calendar to know availability of musicians
• - Automatically providing enquiry price & discount (if applicable)
• - Automating the booking form process (manual) - There's a PDF form I send to the customer after we go back/forth on email on songs/price etc but if more of it could be automated online that would be great. If move to online it would be good to be able to override the set prices with a custom price and also providing a payment gateway
• More Flexibility on pricing - customer selects type of artists they want and it calculates a price based on who they have chosen whether it is a ceremony or canapes or reception (or combination of any). Extra transport fee is added if >50km out of Melbourne.
• How would you re-design this website. Imagine you are a bride/groom looking to book wedding music services. I would love to see some concepts .
• Please indicate any other fees required for your submission and level of support post this competition. I would like this to be an on-going relationship.
Nice to have
• I'd preferably like the website to be in wordpress as I've been familiar with it over time and can do basic updates in the back end. Happy for other suggestions if you can convince me I should move away from wordpress.

```html
<!DOCTYPE html>
<html lang="en">
<head>
<meta charset="utf-8">
<title>Tolly Kessing – Wedding &amp; Event Pianist</title>
<link href="https://fonts.googleapis.com/css2?family=Open+Sans:ital,wght@0,400;0,600;0,700;1,400;1,600&family=Philosopher:ital,wght@1,400;1,700&family=Kaushan+Script&display=swap" rel="stylesheet">
<style>
:root{
  --blue:#2a9fd8;
  --blue-dark:#1d8ac2;
  --ink:#222;
  --text:#5a5a5a;
  --muted:#8a8a8a;
  --grey:#ececec;
  --grey-2:#e2e2e2;
  --white:#fff;
  --footer:#161616;
}
*{box-sizing:border-box;margin:0;padding:0}
html,body{width:1200px;height:3782px;overflow:hidden}
body{position:relative;font-family:'Open Sans',Arial,sans-serif;color:var(--text);background:var(--white)}
.abs{position:absolute}
.photo{position:absolute}
.btn{position:absolute;display:flex;align-items:center;justify-content:center;gap:14px;background:var(--blue);color:var(--white);border-radius:30px;font-weight:600;font-size:18px;box-shadow:0 3px 8px rgba(0,0,0,.15)}
.btn svg{width:16px;height:16px}
.section-title{position:absolute;display:flex;align-items:center;gap:12px;font-size:27px;color:var(--ink);text-transform:uppercase;letter-spacing:.5px}
.section-title .dot{width:30px;height:30px;border-radius:50%;background:var(--ink)}

/* hero */
.hero{position:absolute;left:0;top:0;width:1200px;height:681px;background:linear-gradient(100deg,#2b2a26 0%,#3c3b33 30%,#4f5047 55%,#2f312c 80%,#1f211e 100%)}
.hero .shade{position:absolute;inset:0;background:linear-gradient(90deg,rgba(0,0,0,.15),rgba(0,0,0,.35) 60%,rgba(0,0,0,.2))}
.social-top{position:absolute;left:22px;top:26px;display:flex;gap:10px}
.social-top span{width:14px;height:14px;border-radius:50%;background:rgba(255,255,255,.85)}
.menu{position:absolute;right:22px;top:26px;width:24px}
.menu i{display:block;height:3px;background:var(--white);margin-bottom:5px}
.brand-tab{position:absolute;left:461px;top:0;width:278px;height:88px;background:var(--white);display:flex;align-items:center;justify-content:center;gap:10px;box-shadow:0 2px 8px rgba(0,0,0,.3)}
.brand-tab .mark{width:34px;height:34px;border-radius:50%;background:var(--ink)}
.brand-tab .name{font-weight:700;font-size:22px;color:var(--ink);letter-spacing:.3px}
.hero h1{position:absolute;left:563px;top:246px;font-family:'Philosopher',Georgia,serif;font-style:italic;font-weight:400;font-size:64px;color:var(--white);letter-spacing:3px}
.hero p{position:absolute;left:563px;top:326px;width:470px;font-style:italic;font-size:18px;line-height:31px;color:var(--white);letter-spacing:.9px}

/* intro */
.intro-back{left:101px;top:812px;width:418px;height:282px;background:var(--grey-2)}
.roles{position:absolute;left:582px;top:755px;display:flex;align-items:center;gap:18px;font-family:'Philosopher',Georgia,serif;font-style:italic;font-weight:700;font-size:27px;color:var(--blue);letter-spacing:1px}
.roles .dot{width:30px;height:30px;border-radius:50%;background:var(--ink)}
.intro-text{position:absolute;left:580px;top:816px;width:525px;text-align:center;font-size:15px;line-height:24px;color:var(--text)}
.badge{position:absolute;top:938px;border-radius:50%}

/* music */
.music{position:absolute;left:0;top:1230px;width:1200px;height:623px;background:var(--grey)}
.player{position:absolute;left:68px;top:1379px;width:482px;height:305px;background:var(--white);box-shadow:0 1px 4px rgba(0,0,0,.15)}
.player .cover{position:absolute;left:0;top:0;width:140px;height:140px;background:linear-gradient(135deg,#4a4640,#2a2824)}
.player .play{position:absolute;left:150px;top:10px;width:44px;height:44px;border-radius:50%;background:#f05a24}
.player .play::after{content:"";position:absolute;left:17px;top:13px;border-left:14px solid #fff;border-top:9px solid transparent;border-bottom:9px solid transparent}
.player .track-title{position:absolute;left:202px;top:14px;font-size:14px;color:var(--ink);font-weight:600}
.player .stream{position:absolute;right:14px;top:14px;font-size:10px;color:#999;letter-spacing:1px}
.player .wave{position:absolute;left:150px;top:62px;width:318px;height:58px}
.player .meta{position:absolute;right:14px;top:124px;font-size:10px;color:#999}
.tracks{position:absolute;left:0;top:140px;width:100%}
.tracks li{list-style:none;height:41px;border-top:1px solid #e6e6e6;display:flex;align-items:center;font-size:12px;color:#555;position:relative}
.tracks li .thumb{width:34px;height:34px;margin:0 12px 0 4px;background:#2a2a2a}
.tracks li.active{color:#f05a24}
.tracks li .plays{position:absolute;right:34px;font-size:10px;color:#999}
.music-back{left:615px;top:1364px;width:494px;height:282px;background:var(--white)}

/* events */
.events-back{left:101px;top:1992px;width:418px;height:282px;background:var(--grey-2)}
.events{position:absolute;left:648px;top:1989px;width:481px;border:1px solid #ddd;background:var(--white)}
.event{display:flex;height:68px;border-bottom:1px solid #e2e2e2;position:relative}
.event .date{width:52px;display:flex;flex-direction:column}
.event .day{height:40px;background:var(--blue);color:var(--white);font-weight:700;font-size:24px;display:flex;align-items:center;justify-content:center}
.event .month{flex:1;background:#333;color:var(--white);font-size:12px;display:flex;align-items:center;justify-content:center}
.event .info{padding:7px 0 0 14px;flex:1}
.event .name{font-size:15px;color:#444}
.event .row{display:flex;justify-content:space-between;margin-top:10px;font-size:11px;color:#777;padding-right:22px}
.event .row span{display:flex;align-items:center;gap:5px}
.event svg{width:11px;height:11px}

/* video */
.video-photo{left:0;top:2413px;width:600px;height:396px;background:linear-gradient(110deg,#6d5a48 0%,#a89076 35%,#d8d0c6 60%,#8b7a68 100%)}
.video-play{position:absolute;left:270px;top:2581px;width:70px;height:50px;border-radius:12px;background:#d62b2b}
.video-play::after{content:"";position:absolute;left:27px;top:14px;border-left:20px solid #fff;border-top:11px solid transparent;border-bottom:11px solid transparent}
.video-panel{position:absolute;left:600px;top:2413px;width:600px;height:396px;background:var(--blue);color:var(--white)}
.video-panel h2{position:absolute;left:58px;top:54px;font-weight:400;font-size:31px}
.video-panel p{position:absolute;left:58px;width:500px;font-size:15px;line-height:22px}
.watch{position:absolute;left:60px;top:277px;width:205px;height:43px;background:var(--white);border-radius:22px;display:flex;align-items:center;gap:10px;padding-left:8px;color:var(--ink);font-size:14px;font-weight:700}
.watch .ico{width:28px;height:28px;border-radius:50%;background:var(--blue);position:relative}
.watch .ico::after{content:"";position:absolute;left:11px;top:8px;border-left:9px solid #fff;border-top:6px solid transparent;border-bottom:6px solid transparent}

/* testimonial */
.quote-pill{position:absolute;left:76px;top:2942px;width:1048px;height:294px;background:var(--grey);border-radius:150px}
.quote-photo{left:81px;top:2955px;width:214px;height:214px;border-radius:50%;background:radial-gradient(circle at 45% 40%,#f4ede4,#c9c2b4 65%,#9aa69a);border:6px solid var(--white)}
.quote{position:absolute;left:323px;top:2982px;width:780px;font-style:italic;font-size:14px;line-height:22px;color:#444}
.quote-by{position:absolute;left:323px;top:3110px;display:flex;gap:26px;align-items:baseline;font-size:12px;color:#555}
.quote-by b{font-size:15px;color:var(--ink);letter-spacing:.5px}
.quote-by i{font-style:italic}
.arrow-round{position:absolute;top:3040px;width:38px;height:38px;border-radius:50%;background:var(--grey-2);display:flex;align-items:center;justify-content:center}
.arrow-round svg{width:14px;height:14px}

/* price */
.price-band{position:absolute;left:0;top:3270px;width:1200px;height:189px;background:var(--grey)}
.price-pill{position:absolute;left:418px;top:3312px;width:363px;height:79px;border-radius:40px;background:var(--blue);display:flex;align-items:center;padding-left:40px;color:var(--white);font-family:'Kaushan Script',cursive;font-size:32px}
.price-pill .go{position:absolute;right:14px;top:17px;width:46px;height:46px;border-radius:50%;background:#2c2c2c;display:flex;align-items:center;justify-content:center}
.price-pill .go svg{width:18px;height:18px}
.price-note{position:absolute;left:0;top:3410px;width:1200px;text-align:center;font-size:11px;color:#888;letter-spacing:.5px}

/* footer */
.footer{position:absolute;left:0;top:3459px;width:1200px;height:323px;background:repeating-linear-gradient(90deg,#141414 0 40px,#1b1b1b 40px 80px)}
.footer .mark{position:absolute;left:577px;top:66px;width:46px;height:46px;border-radius:50%;background:#444}
.footer .social{position:absolute;left:0;top:160px;width:1200px;display:flex;justify-content:center;gap:12px}
.footer .social span{width:14px;height:14px;border-radius:50%;background:#ddd}
.footer .contact{position:absolute;left:0;top:204px;width:1200px;display:flex;justify-content:center;gap:60px;color:#ddd;font-size:15px}
.footer .contact span{display:flex;align-items:center;gap:10px}
.footer .contact svg{width:15px;height:15px}
.footer .rule{position:absolute;left:0;top:250px;width:1200px;height:1px;background:#2b2b2b}
.footer .copy{position:absolute;left:0;top:272px;width:1200px;text-align:center;font-size:12px;color:#888}
</style>
</head>
<body>

<!-- Hero -->
<header class="hero">
  <div class="photo" role="img" aria-label="Pianist in a dark suit playing a white grand piano outdoors among trees at dusk" style="inset:0;background:radial-gradient(ellipse at 25% 45%,#5a5a52 0%,#36352f 45%,transparent 70%),radial-gradient(ellipse at 60% 80%,#cfcfca 0%,rgba(207,207,202,.3) 25%,transparent 45%)"></div>
  <div class="shade"></div>
  <div class="social-top"><span></span><span></span><span></span><span></span><span></span></div>
  <div class="menu"><i></i><i></i><i></i></div>
  <div class="brand-tab"><span class="mark"></span><span class="name">TOLLYKESSING</span></div>
  <h1>Tolly Kessing</h1>
  <p>Tolly Kessing is a Melbourne professional pianist with over 5 years experience within the wedding industry and has played piano for more</p>
  <div class="btn" style="left:562px;top:456px;width:187px;height:58px">Book Now <svg viewBox="0 0 16 16"><path d="M2 8h11M9 3l5 5-5 5" stroke="#fff" stroke-width="2.4" fill="none"/></svg></div>
</header>

<!-- Intro -->
<section>
  <div class="abs intro-back"></div>
  <div class="photo" role="img" aria-label="Pianist in a suit holding an award plaque in front of an awards backdrop" style="left:169px;top:741px;width:282px;height:421px;background:linear-gradient(180deg,#6b5a3e,#3a3026 50%,#241d17)"></div>
  <div class="roles">Wedding Pianist <span class="dot"></span> Event Pianist</div>
  <p class="intro-text">Tolly Kessing is Melbourne's premier award wedding &amp; event pianist specialising in playing beautiful background music for weddings, special occasions &amp; corporate events.</p>
  <div class="badge" style="left:676px;width:110px;height:110px;background:#2a2a2a"></div>
  <div class="badge" style="left:792px;width:106px;height:106px;background:#c9a43a"></div>
  <div class="badge" style="left:926px;width:104px;height:104px;background:#a6a8c0"></div>
  <div class="btn" style="left:749px;top:1107px;width:179px;height:50px">Book Now <svg viewBox="0 0 16 16"><path d="M2 8h11M9 3l5 5-5 5" stroke="#fff" stroke-width="2.4" fill="none"/></svg></div>
</section>

<!-- Music -->
<section class="music"></section>
<div class="section-title" style="left:265px;top:1296px"><span class="dot"></span>Music</div>
<div class="player">
  <div class="cover" role="img" aria-label="Album cover artwork"></div>
  <div class="play"></div>
  <div class="track-title">THE BELLBIRDS - ...</div>
  <div class="stream">AUDIOSTREAM</div>
  <svg class="wave" viewBox="0 0 318 58" preserveAspectRatio="none">
    <g fill="#555">
      <rect x="0" y="24" width="3" height="20"/><rect x="6" y="18" width="3" height="26"/><rect x="12" y="14" width="3" height="30"/><rect x="18" y="20" width="3" height="24"/><rect x="24" y="10" width="3" height="34"/><rect x="30" y="16" width="3" height="28"/><rect x="36" y="8" width="3" height="36"/><rect x="42" y="14" width="3" height="30"/><rect x="48" y="12" width="3" height="32"/><rect x="54" y="6" width="3" height="38"/><rect x="60" y="12" width="3" height="32"/><rect x="66" y="10" width="3" height="34"/><rect x="72" y="16" width="3" height="28"/><rect x="78" y="8" width="3" height="36"/><rect x="84" y="12" width="3" height="32"/><rect x="90" y="6" width="3" height="38"/><rect x="96" y="14" width="3" height="30"/><rect x="102" y="10" width="3" height="34"/><rect x="108" y="16" width="3" height="28"/><rect x="114" y="8" width="3" height="36"/><rect x="120" y="12" width="3" height="32"/><rect x="126" y="10" width="3" height="34"/><rect x="132" y="14" width="3" height="30"/><rect x="138" y="6" width="3" height="38"/><rect x="144" y="12" width="3" height="32"/><rect x="150" y="16" width="3" height="28"/><rect x="156" y="10" width="3" height="34"/><rect x="162" y="8" width="3" height="36"/><rect x="168" y="14" width="3" height="30"/><rect x="174" y="12" width="3" height="32"/><rect x="180" y="6" width="3" height="38"/><rect x="186" y="14" width="3" height="30"/><rect x="192" y="10" width="3" height="34"/><rect x="198" y="18" width="3" height="26"/><rect x="204" y="12" width="3" height="32"/><rect x="210" y="8" width="3" height="36"/><rect x="216" y="14" width="3" height="30"/><rect x="222" y="10" width="3" height="34"/><rect x="228" y="16" width="3" height="28"/><rect x="234" y="12" width="3" height="32"/><rect x="240" y="8" width="3" height="36"/><rect x="246" y="14" width="3" height="30"/><rect x="252" y="18" width="3" height="26"/><rect x="258" y="12" width="3" height="32"/><rect x="264" y="16" width="3" height="28"/><rect x="270" y="20" width="3" height="24"/><rect x="276" y="14" width="3" height="30"/><rect x="282" y="18" width="3" height="26"/><rect x="288" y="22" width="3" height="22"/><rect x="294" y="20" width="3" height="24"/><rect x="300" y="26" width="3" height="18"/><rect x="306" y="24" width="3" height="20"/><rect x="312" y="28" width="3" height="16"/>
    </g>
    <rect x="296" y="40" width="22" height="10" fill="#333"/>
  </svg>
  <div class="meta">&#9654; 139K</div>
  <ul class="tracks">
    <li class="active"><span class="thumb"></span>THE BELLBIRDS - HARBOUR LIGHTS<span class="plays">&#9654; 139K</span></li>
    <li><span class="thumb"></span>JON FAIRLIE - PAPER LANTERNS<span class="plays">&#9654; 139K</span></li>
    <li><span class="thumb"></span>JON FAIRLIE - PAPER LANTERNS<span class="plays">&#9654; 139K</span></li>
    <li><span class="thumb"></span>JON FAIRLIE - PAPER LANTERNS<span class="plays">&#9654; 139K</span></li>
  </ul>
</div>
<div class="btn" style="left:245px;top:1722px;width:158px;height:50px">More <svg viewBox="0 0 16 16"><path d="M2 8h11M9 3l5 5-5 5" stroke="#fff" stroke-width="2.4" fill="none"/></svg></div>
<div class="abs music-back"></div>
<div class="photo" role="img" aria-label="Pianist at an upright piano beside a cellist in a black dress" style="left:686px;top:1296px;width:353px;height:421px;background:linear-gradient(180deg,#e6e2dc 0%,#8a7a6a 45%,#3a2f2a 100%)"></div>

<!-- Events -->
<div class="abs events-back"></div>
<div class="photo" role="img" aria-label="Cellist and pianist standing with a cello beside a vintage white wedding car on a lawn" style="left:169px;top:1923px;width:282px;height:422px;background:linear-gradient(180deg,#8d8a78 0%,#5a5a48 50%,#4a4436 100%)"></div>
<div class="section-title" style="left:746px;top:1918px"><span class="dot"></span>Upcoming Events</div>
<div class="events">
  <div class="event"><div class="date"><span class="day">22</span><span class="month">July</span></div><div class="info"><div class="name">Private event – Aspendale (tbc)</div><div class="row"><span><svg viewBox="0 0 12 12"><path d="M6 0a4 4 0 0 0-4 4c0 3 4 8 4 8s4-5 4-8a4 4 0 0 0-4-4z" fill="#555"/></svg>Decibel Lorem Ipsum</span><span><svg viewBox="0 0 12 12"><circle cx="6" cy="6" r="5" fill="none" stroke="#555" stroke-width="1.5"/><path d="M6 3v3l2 1.5" stroke="#555" stroke-width="1.3" fill="none"/></svg>2:00 pm - 3:00 pm</span></div></div></div>
  <div class="event"><div class="date"><span class="day">24</span><span class="month">July</span></div><div class="info"><div class="name">Private event – Aspendale (tbc)</div><div class="row"><span><svg viewBox="0 0 12 12"><path d="M6 0a4 4 0 0 0-4 4c0 3 4 8 4 8s4-5 4-8a4 4 0 0 0-4-4z" fill="#555"/></svg>Decibel Lorem Ipsum</span><span><svg viewBox="0 0 12 12"><circle cx="6" cy="6" r="5" fill="none" stroke="#555" stroke-width="1.5"/><path d="M6 3v3l2 1.5" stroke="#555" stroke-width="1.3" fill="none"/></svg>2:00 pm - 3:00 pm</span></div></div></div>
  <div class="event"><div class="date"><span class="day">25</span><span class="month">July</span></div><div class="info"><div class="name">Private event – Aspendale (tbc)</div><div class="row"><span><svg viewBox="0 0 12 12"><path d="M6 0a4 4 0 0 0-4 4c0 3 4 8 4 8s4-5 4-8a4 4 0 0 0-4-4z" fill="#555"/></svg>Decibel Lorem Ipsum</span><span><svg viewBox="0 0 12 12"><circle cx="6" cy="6" r="5" fill="none" stroke="#555" stroke-width="1.5"/><path d="M6 3v3l2 1.5" stroke="#555" stroke-width="1.3" fill="none"/></svg>2:00 pm - 3:00 pm</span></div></div></div>
  <div class="event" style="border-bottom:0"><div class="date"><span class="day">26</span><span class="month">July</span></div><div class="info"><div class="name">Private event – Aspendale (tbc)</div><div class="row"><span><svg viewBox="0 0 12 12"><path d="M6 0a4 4 0 0 0-4 4c0 3 4 8 4 8s4-5 4-8a4 4 0 0 0-4-4z" fill="#555"/></svg>Decibel Lorem Ipsum</span><span><svg viewBox="0 0 12 12"><circle cx="6" cy="6" r="5" fill="none" stroke="#555" stroke-width="1.5"/><path d="M6 3v3l2 1.5" stroke="#555" stroke-width="1.3" fill="none"/></svg>2:00 pm - 3:00 pm</span></div></div></div>
</div>
<div class="btn" style="left:807px;top:2297px;width:166px;height:50px">More <svg viewBox="0 0 16 16"><path d="M2 8h11M9 3l5 5-5 5" stroke="#fff" stroke-width="2.4" fill="none"/></svg></div>

<!-- Video -->
<div class="photo video-photo" role="img" aria-label="Pianist playing in the foreground while a wedding couple stands behind"></div>
<div class="video-play"></div>
<section class="video-panel">
  <h2>Wedding Canapes Highlights</h2>
  <p style="top:116px">Lorem ipsum dolor sit amet, consectetuer adipiscing elit. Nam cursus. Morbi ut mi. Nullam enim leo, egestas id, condimentum at, laoreet mattis, massa. Sed eleifend nonummy diam.</p>
  <p style="top:204px">Lorem ipsum dolor sit amet, consectetuer adipiscing lit leo, condimentum at, laoreet mattis, massa.</p>
  <div class="watch"><span class="ico"></span>WATCH THE VIDEO</div>
</section>

<!-- Testimonial -->
<div class="section-title" style="left:470px;top:2878px"><span class="dot"></span>Testimonial</div>
<div class="arrow-round" style="left:12px"><svg viewBox="0 0 14 14"><path d="M9 2L4 7l5 5" stroke="#666" stroke-width="2" fill="none"/></svg></div>
<div class="arrow-round" style="left:1150px"><svg viewBox="0 0 14 14"><path d="M5 2l5 5-5 5" stroke="#666" stroke-width="2" fill="none"/></svg></div>
<div class="quote-pill"></div>
<div class="photo quote-photo" role="img" aria-label="Wedding couple portrait in a round frame"></div>
<p class="quote">" Tolly played at our wedding in April, and provided the perfect soundtrack to our special day. Tolly was very professional and was able to play a broad range of music, including classical hymns for the processional and modern music for other parts of the ceremony.<br>He played beautifully and a number of our guests commented on the ambience created by having a live pianist play during the wedding. I wouldn't hesitate to recommend Tolly for any special occasion.iudicabit nam. "</p>
<div class="quote-by"><b>CLARA AND JAMES</b><i>June 27 2016</i><span>Doncaster East</span></div>

<!-- Price -->
<section class="price-band"></section>
<div class="price-pill">Ceremony price<span class="go"><svg viewBox="0 0 16 16"><path d="M2 8h11M9 3l5 5-5 5" stroke="#fff" stroke-width="2.4" fill="none"/></svg></span></div>
<p class="price-note">Winter Wedding 5% Discount July-Sept (2017 &amp; 2018)</p>

<!-- Footer -->
<footer class="footer">
  <span class="mark"></span>
  <div class="social"><span></span><span></span><span></span><span></span><span></span></div>
  <div class="contact">
    <span><svg viewBox="0 0 16 16"><path d="M3 1l3 3-2 2c1 2 3 4 5 5l2-2 3 3-2 3C6 15 1 10 1 3z" fill="#ddd"/></svg>0400 555 812</span>
    <span><svg viewBox="0 0 16 16"><path d="M1 7l14-6-5 14-2-6z" fill="#ddd"/></svg>tollythepianoman@mailbox.com</span>
  </div>
  <div class="rule"></div>
  <p class="copy">Copyright © 2017  Tolly Kessing. All rights reserved.</p>
</footer>

</body>
</html>
```